Marktplatz Flohmarkt Kleinanzeigen Marktplatz
Zielgruppe
Wir sind ein Marktplatz rund um Hochzeit. D.h. bei uns können kostenlos alle Sachen (Brautkleid, Brautschuhe, Braut Accessories, Hochzeits Dekoration) zum verkauf eingestellt werden. Wie tauscho inserate, nur eben spezialisiert auf Hochzeit
Aufgabenstellung
Wir benötigen für unseren PHP Marktplatz ein Design, welches sehr Modern und ansprechend ist. Wir möchten kein Klassisches Hochzeitsportal mit den Üblichen Rosa, Beigen Farben sein, sondern möchten vor allem die Junge Zielgruppe ansprechen.
Das Design soll ein Mix aus tauscho-inserate und Stoffwandel sein, wobei uns wichtiger wäre das man sich bewusst am design von Stoffwandel orientiert.
Was uns besonders an Stoffwandel gefällt ist im Header die farbliche Leiste wo Logo und Kategorien integriert sind. Schicht und einfach, ohne schnickschnack.
ebenso wie bei Stoffwandel wird bei uns auf der Startseite folgendes integriert:
-Werbung (Banner)
-Plaudernetz
-Forum
Aktuelle menüs auf der Startseite:
-Home
-Marktplatz
-Gesuche (wobei gesuche kann im Layout integriert werden)
-Dienstleister (Händler und Dienstleister)
-Gruppen (das kann en einer anderen Stelle integriert werden)
-Forum (noch nicht integriert, aber beachten beim Layout, da es eingebaut wird)
-Veranstaltungen / Events
-Über Uns
(alles was aktuell im Screenshot zu sehen ist, wird aus der Leiste entfernt und im Footer eingebaut)
Anhang:
-Logo
-Screenshot unseres Aktuellen marktplatzes (noch nicht Online)
-Screenshot von StoffWandel
Design:
-Startseite
-Artikelseite (wenn der Private Kunde eine anzeige einstellt)
-Ansprechende Anmeldeseite inkl. Darstellung unserer Pakete für Privat / Händler / Dienstleister

```html
<!DOCTYPE html>
<html lang="de">
<head>
<meta charset="utf-8">
<title>Schleierbörse – Marktplatz</title>
<link href="https://fonts.googleapis.com/css2?family=Roboto:wght@400;500;700&display=swap" rel="stylesheet">
<style>
:root{
  --pink:#e2007a;
  --pink-dark:#b0005e;
  --bg:#eeeeee;
  --white:#ffffff;
  --grey-text:#666666;
  --grey-light:#9a9a9a;
  --tag-grey:#c8c8c8;
  --line:#e6e6e6;
  --active:#ececec;
}
*{box-sizing:border-box;margin:0;padding:0}
html,body{width:917px;height:1200px;overflow:hidden;background:var(--bg)}
body{font-family:"Roboto",Arial,sans-serif;color:var(--grey-text)}
.page{position:relative;width:1250px;height:1636px;transform:scale(0.73361);transform-origin:0 0;background:var(--bg)}
.abs{position:absolute}

.util-links{top:6px;right:130px;font-size:12px;color:var(--pink)}
.util-links span{margin:0 6px}

.masthead{top:27px;left:0;width:1250px;height:75px;background:var(--pink)}
.brand{left:120px;top:13px;width:130px;color:var(--white);font-size:23px;font-weight:700;line-height:24px;display:flex;align-items:center;gap:8px}
.brand-dot{flex:none;width:12px;height:12px;background:var(--white);border-radius:50%}
.main-nav{left:266px;top:29px;display:flex;font-size:14px;color:var(--white)}
.main-nav a{color:var(--white);text-decoration:none;margin-right:35px}
.search{left:883px;top:21px;width:237px;height:35px;background:var(--white);border-radius:18px}
.search svg{position:absolute;right:16px;top:10px}

.list-head{left:120px;top:134px;width:762px;height:55px;background:var(--white);box-shadow:0 1px 2px rgba(0,0,0,.08)}
.list-head h1{position:absolute;left:26px;top:18px;font-size:18px;font-weight:400;color:#8a8a8a}
.sort{position:absolute;right:40px;top:19px;display:flex;align-items:center;font-size:12px;color:var(--grey-light)}
.sort .pill{background:var(--pink);color:var(--white);border-radius:12px;padding:5px 6px;margin:0 14px 0 11px}

.col{position:absolute;top:205px;width:242px;display:flex;flex-direction:column;gap:15px}
.card{background:var(--white);box-shadow:0 1px 2px rgba(0,0,0,.08)}
.photo{position:relative}
.photo .price{position:absolute;left:0;bottom:0;width:85px;height:39px;background:var(--pink);color:var(--white);font-size:16px;line-height:39px;padding-left:16px}
.photo .cat{position:absolute;right:0;bottom:0;width:88px;height:25px;background:var(--tag-grey);color:var(--white);font-size:12px;line-height:25px;text-align:center}
.card-body{height:82px;padding:12px 16px 0}
.card-body h2{font-size:14px;font-weight:700;color:var(--pink);line-height:17px;letter-spacing:.2px}
.meta{display:flex;justify-content:space-between;font-size:12px;margin-top:5px;color:#555}
.actions{display:flex;height:47px;border-top:1px solid var(--line)}
.actions div{flex:1;display:flex;align-items:center;justify-content:center}
.actions div+div{border-left:1px solid var(--line)}

.img-light{background:linear-gradient(160deg,#f4f4f4,#dedede)}
.img-warm{background:linear-gradient(160deg,#c9b39c,#efe9e2)}
.img-grey{background:linear-gradient(160deg,#a9abb0,#d9dadd)}
.img-green{background:linear-gradient(160deg,#3f6a2c,#8aa06e 55%,#e8e8e4)}

.side{left:907px;width:213px}
.box{background:var(--white);box-shadow:0 1px 2px rgba(0,0,0,.08)}
.box-head{height:56px;background:var(--pink);color:var(--white);font-size:18px;line-height:56px;padding-left:26px}
.cat-list{list-style:none;padding:0 8px}
.cat-list li{height:36px;line-height:36px;font-size:12px;color:#555;border-bottom:1px solid var(--line);padding-left:12px;position:relative}
.cat-list li::after{content:"";position:absolute;right:10px;top:16px;border:3px solid transparent;border-top-color:#c4c4c4}
.cat-list li.all{background:var(--active);color:var(--pink);border:none}
.cat-list li.all::after{display:none}
.ad{background:var(--pink);color:var(--white);text-align:center;height:199px}
.ad h3{font-size:18px;font-weight:500;padding-top:19px}
.ad p{font-size:12px;line-height:20px;margin:22px 18px 0}
.ad .btn{display:inline-block;margin-top:20px;width:145px;height:32px;line-height:32px;border-radius:16px;background:var(--pink-dark);color:#e03a93;font-size:12px;font-weight:700}
.box-text{font-size:12px;line-height:20px;color:#555;padding:10px 20px 0}
.field{margin:0 8px;height:34px;border:1px solid var(--line);border-radius:17px;font-size:12px;color:#999;line-height:32px;padding-left:10px;position:relative}
.send{margin:6px 8px 0 auto;width:104px;height:32px;border-radius:16px;background:var(--pink);color:var(--white);font-size:13px;font-weight:700;text-align:center;line-height:32px}
.share .field{margin-bottom:6px}
.share .field span{position:absolute;right:-1px;top:-1px;width:46px;height:34px;border-radius:17px;background:var(--pink)}
.legal{font-size:12px;color:#555;line-height:14px}
.legal-links{font-size:10px;color:#555;line-height:13px;margin-top:14px}
.legal-links span{margin-right:10px;white-space:nowrap}
.more{left:428px;top:1568px;width:145px;height:33px;border-radius:17px;background:var(--white);box-shadow:0 1px 3px rgba(0,0,0,.12);color:var(--pink);font-size:12px;font-weight:700;text-align:center;line-height:33px}
</style>
</head>
<body>
<div class="page">
  <div class="abs util-links">Hilfe<span>|</span>Anmelden<span>|</span>Warenkorb (0)</div>

  <header class="abs masthead">
    <div class="abs brand"><span class="brand-dot"></span><span>Schleier<br>börse</span></div>
    <nav class="abs main-nav">
      <a>Marktplatz</a><a>Dienstleister</a><a>Gruppen</a><a>Forum</a><a>Veranstaltungen</a><a>Über uns</a>
    </nav>
    <div class="abs search">
      <svg width="15" height="15" viewBox="0 0 15 15"><circle cx="6" cy="6" r="4.5" fill="none" stroke="#aaa" stroke-width="2"/><line x1="9.5" y1="9.5" x2="13.5" y2="13.5" stroke="#aaa" stroke-width="2"/></svg>
    </div>
  </header>

  <section class="abs list-head">
    <h1>Marktplatz</h1>
    <div class="sort">Sortieren nach:<span class="pill">Datum</span>Preis</div>
  </section>

  <svg width="0" height="0" style="position:absolute">
    <defs>
      <symbol id="icon-cart" viewBox="0 0 20 18"><path d="M1 2h3l2.5 9h9l2-6H5.5" fill="none" stroke="#a0a0a0" stroke-width="1.6"/><circle cx="8" cy="15" r="1.6" fill="#a0a0a0"/><circle cx="14" cy="15" r="1.6" fill="#a0a0a0"/></symbol>
      <symbol id="icon-search" viewBox="0 0 14 14"><circle cx="6" cy="6" r="4" fill="none" stroke="#a0a0a0" stroke-width="1.8"/><line x1="9" y1="9" x2="12.5" y2="12.5" stroke="#a0a0a0" stroke-width="2"/></symbol>
    </defs>
  </svg>

  <div class="col" style="left:120px">
    <article class="card"><div class="photo img-light" style="height:293px" role="img" aria-label="Kurzes weißes Brautkleid mit Volants"><span class="price">69,00 €</span><span class="cat">Brautmode</span></div><div class="card-body"><h2>Traumhaftes Hochzeitskleid in weiß</h2><div class="meta"><span>22.08.2014</span><span>Köln/ Altstadt</span></div></div><div class="actions"><div><svg width="20" height="18"><use href="#icon-cart"/></svg></div><div><svg width="14" height="14"><use href="#icon-search"/></svg></div></div></article>
    <article class="card"><div class="photo img-warm" style="height:368px" role="img" aria-label="Langes Brautkleid mit Stickerei"><span class="price">69,00 €</span><span class="cat">Brautmode</span></div><div class="card-body"><h2>Traumhaftes Hochzeitskleid in weiß</h2><div class="meta"><span>22.08.2014</span><span>Köln/ Altstadt</span></div></div><div class="actions"><div><svg width="20" height="18"><use href="#icon-cart"/></svg></div><div><svg width="14" height="14"><use href="#icon-search"/></svg></div></div></article>
    <article class="card"><div class="photo img-light" style="height:254px" role="img" aria-label="Brautkleid mit Raffungen, Rückansicht"><span class="price">69,00 €</span><span class="cat">Brautmode</span></div><div class="card-body"><h2>Traumhaftes Hochzeitskleid in weiß</h2><div class="meta"><span>22.08.2014</span><span>Köln/ Altstadt</span></div></div><div class="actions"><div><svg width="20" height="18"><use href="#icon-cart"/></svg></div><div><svg width="14" height="14"><use href="#icon-search"/></svg></div></div></article>
  </div>

  <div class="col" style="left:380px">
    <article class="card"><div class="photo img-light" style="height:254px" role="img" aria-label="Brautkleid mit Raffungen, Rückansicht"><span class="price">69,00 €</span><span class="cat">Brautmode</span></div><div class="card-body"><h2>Traumhaftes Hochzeitskleid in weiß</h2><div class="meta"><span>22.08.2014</span><span>Köln/ Altstadt</span></div></div><div class="actions"><div><svg width="20" height="18"><use href="#icon-cart"/></svg></div><div><svg width="14" height="14"><use href="#icon-search"/></svg></div></div></article>
    <article class="card"><div class="photo img-grey" style="height:293px" role="img" aria-label="Kurzes Spitzenbrautkleid"><span class="price">69,00 €</span><span class="cat">Brautmode</span></div><div class="card-body"><h2>Traumhaftes Hochzeitskleid in weiß</h2><div class="meta"><span>22.08.2014</span><span>Köln/ Altstadt</span></div></div><div class="actions"><div><svg width="20" height="18"><use href="#icon-cart"/></svg></div><div><svg width="14" height="14"><use href="#icon-search"/></svg></div></div></article>
    <article class="card"><div class="photo img-green" style="height:368px" role="img" aria-label="Brautkleid im Freien vor Bäumen"><span class="price">69,00 €</span><span class="cat">Brautmode</span></div><div class="card-body"><h2>Traumhaftes Hochzeitskleid in weiß</h2><div class="meta"><span>22.08.2014</span><span>Köln/ Altstadt</span></div></div><div class="actions"><div><svg width="20" height="18"><use href="#icon-cart"/></svg></div><div><svg width="14" height="14"><use href="#icon-search"/></svg></div></div></article>
  </div>

  <div class="col" style="left:640px">
    <article class="card"><div class="photo img-green" style="height:368px" role="img" aria-label="Brautkleid im Freien vor Bäumen"><span class="price">69,00 €</span><span class="cat">Brautmode</span></div><div class="card-body"><h2>Traumhaftes Hochzeitskleid in weiß</h2><div class="meta"><span>22.08.2014</span><span>Köln/ Altstadt</span></div></div><div class="actions"><div><svg width="20" height="18"><use href="#icon-cart"/></svg></div><div><svg width="14" height="14"><use href="#icon-search"/></svg></div></div></article>
    <article class="card"><div class="photo img-grey" style="height:254px" role="img" aria-label="Drapiertes Brautkleid mit Blüte"><span class="price">69,00 €</span><span class="cat">Brautmode</span></div><div class="card-body"><h2>Traumhaftes Hochzeitskleid in weiß</h2><div class="meta"><span>22.08.2014</span><span>Köln/ Altstadt</span></div></div><div class="actions"><div><svg width="20" height="18"><use href="#icon-cart"/></svg></div><div><svg width="14" height="14"><use href="#icon-search"/></svg></div></div></article>
    <article class="card"><div class="photo img-light" style="height:293px" role="img" aria-label="Kurzes weißes Brautkleid mit Volants"><span class="price">69,00 €</span><span class="cat">Brautmode</span></div><div class="card-body"><h2>Traumhaftes Hochzeitskleid in weiß</h2><div class="meta"><span>22.08.2014</span><span>Köln/ Altstadt</span></div></div><div class="actions"><div><svg width="20" height="18"><use href="#icon-cart"/></svg></div><div><svg width="14" height="14"><use href="#icon-search"/></svg></div></div></article>
  </div>

  <div class="abs more">Mehr anzeigen</div>

  <aside class="abs side box" style="top:134px;height:359px">
    <div class="box-head">Kategorien</div>
    <ul class="cat-list">
      <li>Brautmode</li><li>Schuhe</li><li>Accessoires</li><li>Formwäsche/ Dessous</li><li>Bräutigam</li><li>Empfang &amp; Geschenke</li><li>Dekoration</li><li class="all">Alle Kategorien</li>
    </ul>
  </aside>

  <aside class="abs side ad" style="top:508px">
    <h3>Anzeige aufgeben</h3>
    <p>Lorem ipsum dolor sit amet, con-setetur sadipscing elitr, sed diam nonumy eirmod tempor invidunt</p>
    <span class="btn">Neu Registrieren</span>
  </aside>

  <aside class="abs side box" style="top:722px;height:205px">
    <div class="box-head">Newsletter</div>
    <p class="box-text" style="height:61px">Jetzt anmelden und kein Ange-bot mehr verpassen</p>
    <div class="field">Emailadresse</div>
    <div class="send">Absenden</div>
  </aside>

  <aside class="abs side box share" style="top:941px;height:264px">
    <div class="box-head">Seite empfehlen</div>
    <p class="box-text" style="height:79px">Empfehlen und teilen Sie<br>unsere Seite mit Ihren Freund-<br>en und Bekannten</p>
    <div class="field">Empfehlen auf<span></span></div>
    <div class="field">Teilen auf<span></span></div>
    <div class="field">Empfehlen auf<span></span></div>
  </aside>

  <footer class="abs side" style="top:1219px">
    <p class="legal">© 2014 schleierboerse.de. Alle Rechte vorbehalten.</p>
    <p class="legal-links"><span>Über Uns</span><span>Impressum</span><span>Presse</span><span>Jobs</span><br><span>Kontakt</span><span>FAQ</span><span>Datenschutzrichtlinie</span><br><span>Rechtliche Hinweise</span></p>
  </footer>
</div>
</body>
</html>
```